Medical business needs responsive Bootstrap theme design

We need a responsive Twitter Bootstrap theme for a hair transplant business in South Korea which looks good from full size desktop screens down to smartphone displays. We would like the site to match in style with our brochure design (see the PDF and Adobe Illustrator files), although it does not need to match exactly. Please feel free to use the design elements and images in the brochure. The general flow of the theme is shown in the wireframe image.
We expect graphic design, images, CSS, and HTML. No PHP/backend/ecommerce integration is expected.
Here are the links to the 3 stock images in the brochure:
http://www.pixelvantry.com/pic.mhtml?id=918270563
http://www.lumoframes.com/photo/hair-transplant-gm730418256-61920475
http://www.lumoframes.com/photo/doctor-inspecting-skin-of-head-gm842067319-57301846
You can use the Bootstrap template here as a starting point: http://kelvarnlayouts.com/template-overviews/agency/
Target Market(s)
Our primary customers will be Westerners aged 28-45
Industry/Entity Type
Plastic Surgery
Coding
Coded - Design and coding required
Number of Pages Required
1 page

```html
<!DOCTYPE html>
<html lang="en">
<head>
<meta charset="utf-8">
<title>Hanul Hair Restoration Center</title>
<link rel="stylesheet" href="https://fonts.googleapis.com/css2?family=Raleway:ital,wght@0,400;0,500;0,600;0,700;1,700&family=Open+Sans:wght@400;600&display=swap">
<style>
:root{
  --blue:#3f87c9;
  --blue-deep:#2f6fae;
  --dark:#444347;
  --darker:#3a393d;
  --text:#333;
  --muted:#666;
  --row-a:#e9e9e9;
  --row-b:#f5f5f5;
  --panel:#e7e7e7;
  --white:#fff;
}
*{box-sizing:border-box;margin:0;padding:0}
html,body{width:1200px;height:3644px;overflow:hidden}
body{position:relative;background:var(--white);font-family:"Open Sans",Arial,sans-serif;color:var(--text)}
section,header,footer{position:absolute;left:0;width:1200px}
.abs{position:absolute}
.section-title{position:absolute;left:0;width:100%;text-align:center;font-family:"Raleway",sans-serif;font-weight:500;font-size:32px;color:#222}
.divider{position:absolute;left:50%;width:140px;margin-left:-70px;height:20px}
.divider::before,.divider::after{content:"";position:absolute;top:9px;width:48px;height:2px;background:var(--blue)}
.divider::before{left:0}.divider::after{right:0}
.divider span{position:absolute;left:60px;top:0;width:20px;height:20px;border-radius:50%;border:3px solid var(--blue)}
.on-dark .section-title{color:var(--white)}
.on-dark .divider::before,.on-dark .divider::after{background:var(--white)}
.on-dark .divider span{border-color:var(--white)}

/* hero */
.hero{top:0;height:651px;background:linear-gradient(115deg,#8f8a86 0%,#b7b0aa 35%,#ddd8d3 60%,#c9c4c0 100%)}
.topbar{top:0;height:110px;background:rgba(63,135,201,.92)}
.brand{position:absolute;left:97px;top:26px;display:flex;align-items:center;gap:16px}
.brand-mark{width:58px;height:58px;border-radius:50%;border:4px solid var(--white)}
.brand-name{font-family:"Raleway",sans-serif;font-weight:600;font-size:24px;color:var(--white);line-height:1.1;width:230px}
.menu-toggle{position:absolute;left:1065px;top:40px;width:36px;height:30px;border:2px solid rgba(255,255,255,.8);border-radius:4px}
.menu-toggle i{position:absolute;left:8px;width:16px;height:2px;background:var(--white)}
.hero-title{position:absolute;left:97px;top:176px;font-family:"Raleway",sans-serif;font-weight:700;font-style:italic;font-size:36px;color:var(--white)}
.hero-sub{position:absolute;left:97px;top:226px;font-family:"Raleway",sans-serif;font-size:21px;color:var(--white)}
.dots{position:absolute;left:1026px;top:618px;display:flex;gap:17px}
.dots i{width:10px;height:10px;border-radius:50%;background:#2b2b2b}
.dots i.active{background:var(--blue)}

/* why */
.why{top:651px;height:515px}
.feature{position:absolute;top:189px;width:292px;height:282px;color:var(--white);text-align:center;border-radius:3px}
.feature.blue{background:var(--blue)}
.feature.dark{background:var(--dark)}
.feature-icon{position:absolute;left:105px;top:-56px;width:84px;height:84px;border-radius:50%;border:4px solid var(--white);display:flex;align-items:center;justify-content:center}
.feature.blue .feature-icon{background:var(--dark)}
.feature.dark .feature-icon{background:var(--blue)}
.feature h3{position:absolute;top:60px;width:100%;font-family:"Raleway",sans-serif;font-weight:600;font-size:18px}
.feature p{position:absolute;left:34px;width:224px;font-size:13px;line-height:17px}
.feature .p1{top:102px}.feature .p2{top:159px}
.btn{position:absolute;left:91px;top:248px;width:110px;height:32px;font-size:12px;line-height:32px;color:var(--white);border-radius:2px}
.feature.blue .btn{background:var(--dark)}
.feature.dark .btn{background:var(--blue)}

/* methods */
.methods{top:1166px;height:590px;background:var(--blue);color:var(--white)}
.methods-intro{position:absolute;top:99px;left:0;width:100%;text-align:center;font-size:13px;line-height:21px}
.method{position:absolute;top:195px;width:500px}
.method h4{font-family:"Raleway",sans-serif;font-weight:500;font-size:17px}
.method .lede{font-size:12px;margin-top:8px}
.steps{position:absolute;top:58px;left:0;width:401px;height:291px}
.step-head{position:absolute;left:0;width:263px;height:46px;background:var(--dark);font-size:13px;line-height:46px;padding-left:13px}
.step-head::after{content:"";position:absolute;right:14px;top:20px;border-left:5px solid transparent;border-right:5px solid transparent;border-top:6px solid var(--white)}
.step-head.closed{height:48px;line-height:48px;border-top:1px solid #5a595d}
.step-head.closed::after{top:19px;border-top:5px solid transparent;border-bottom:5px solid transparent;border-left:6px solid var(--white);border-right:0}
.step-body{position:absolute;left:0;top:46px;width:401px;height:148px;background:var(--darker)}
.step-art{position:absolute;left:0;top:0;width:263px;height:148px;background:linear-gradient(90deg,#b9b9bb 0%,#dcdcdc 45%,#e6c9b9 70%,#d9b3a0 100%)}
.step-text{position:absolute;left:273px;top:10px;width:120px;font-size:11px;line-height:18px;text-align:left}

/* comparison */
.comparison{top:1756px;height:474px}
.compare-table{position:absolute;left:97px;top:114px;width:1006px;border-collapse:collapse;font-size:12.5px}
.compare-table th{background:var(--blue);color:var(--white);font-weight:400;text-align:left;height:39px;padding-left:13px}
.compare-table td{height:39px;padding-left:13px;color:#444;border-right:2px solid var(--white)}
.compare-table tr:nth-child(odd) td{background:var(--row-a)}
.compare-table tr:nth-child(even) td{background:var(--row-b)}
.compare-table .c1{width:377px}.compare-table .c2{width:381px}

/* contact */
.contact{top:2230px;height:413px}
.contact-photo{position:absolute;left:0;top:0;width:675px;height:413px;background:linear-gradient(120deg,#7fa7cc 0%,#5f8fbd 40%,#4a7db0 100%)}
.contact-panel{position:absolute;left:675px;top:0;width:525px;height:413px;background:var(--panel)}
.contact-panel .section-title{top:14px}
.field{position:absolute;left:39px;width:369px;height:37px;border:1px solid #8a8a8a;border-radius:3px;background:var(--panel);font-size:12px;color:#444;padding:10px 8px}
.field.message{height:63px}
.submit{position:absolute;left:39px;top:347px;width:146px;height:34px;background:var(--dark);color:var(--white);font-size:13px;line-height:34px;text-align:center;border-radius:2px}
.social{position:absolute;top:349px;width:30px;height:30px;border:1.5px solid #555;border-radius:50%}

/* testimonials */
.testimonials{top:2643px;height:454px}
.testimonial{position:absolute;top:124px;width:316px;height:289px;border:2px solid #a9c6e4;background:var(--white)}
.testimonial-photo{position:absolute;left:5px;top:5px;width:302px;height:177px}
.ba-bar{position:absolute;left:5px;top:182px;width:302px;height:42px;background:var(--blue);color:var(--white);font-size:13px;display:flex}
.ba-bar span{flex:1;text-align:center;line-height:42px}
.ba-bar span+span{border-left:1px solid rgba(255,255,255,.6)}
.testimonial p{position:absolute;left:14px;top:237px;width:284px;text-align:center;font-size:12px;line-height:18px}

/* blog */
.blog{top:3097px;height:486px;background:var(--dark)}
.post{position:absolute;top:126px;width:296px;height:323px;background:var(--white)}
.post-photo{position:absolute;left:0;top:0;width:296px;height:161px}
.post h5{position:absolute;left:12px;top:182px;font-size:13.5px;font-weight:600;color:#222}
.post p{position:absolute;left:12px;top:207px;width:272px;font-size:12px;line-height:18px;color:#333}
.post .more{position:absolute;left:12px;top:280px;width:80px;height:25px;border:1px solid #777;border-radius:3px;font-size:11.5px;line-height:23px;text-align:center}

.footer{top:3583px;height:61px;background:var(--blue);color:var(--white);text-align:center;font-size:12px;line-height:61px}
</style>
</head>
<body>

<section class="hero">
  <div class="abs" style="left:0;top:0;width:1200px;height:651px" role="img" aria-label="Photo of a female doctor examining a man's scalp with a magnifying glass"></div>
  <div class="hero-title">Hanul Hair Restoration Center</div>
  <div class="hero-sub">Hair Restoration Surgery</div>
  <div class="dots"><i></i><i class="active"></i><i></i></div>
</section>

<header class="topbar">
  <div class="brand"><span class="brand-mark"></span><span class="brand-name">Hanul Hair Restoration Center</span></div>
  <div class="menu-toggle"><i style="top:8px"></i><i style="top:13px"></i><i style="top:18px"></i></div>
</header>

<section class="why">
  <h2 class="section-title" style="top:32px">Why South Korea?</h2>
  <div class="divider" style="top:78px"><span></span></div>

  <div class="feature blue" style="left:97px">
    <div class="feature-icon"><svg width="40" height="40" viewBox="0 0 40 40"><path d="M9 21l8 8 15-17" fill="none" stroke="#fff" stroke-width="4" stroke-linecap="round" stroke-linejoin="round"/></svg></div>
    <h3>Quality of Care</h3>
    <p class="p1">Hair Restoration Surgery has improved significantly over the last decade.</p>
    <p class="p2">State-of-the-art technology ensures transplanted hair is strategically placed for a natural look.</p>
    <div class="btn">Read More</div>
  </div>
  <div class="feature dark" style="left:454px">
    <div class="feature-icon"><svg width="44" height="44" viewBox="0 0 44 44"><circle cx="22" cy="22" r="17" fill="none" stroke="#fff" stroke-width="3"/><path d="M22 11v11l7 5" fill="none" stroke="#fff" stroke-width="3" stroke-linecap="round"/></svg></div>
    <h3>Convenience</h3>
    <p class="p1">Hair Restoration Surgery has improved significantly over the last decade.</p>
    <p class="p2">State-of-the-art technology ensures transplanted hair is strategically placed for a natural look.</p>
    <div class="btn">Read More</div>
  </div>
  <div class="feature dark" style="left:811px">
    <div class="feature-icon"><svg width="44" height="44" viewBox="0 0 44 44"><circle cx="22" cy="22" r="16" fill="none" stroke="#fff" stroke-width="3"/><circle cx="22" cy="22" r="8" fill="none" stroke="#fff" stroke-width="3"/></svg></div>
    <h3>Cost Savings</h3>
    <p class="p1">Hair Restoration Surgery has improved significantly over the last decade.</p>
    <p class="p2">State-of-the-art technology ensures transplanted hair is strategically placed for a natural look.</p>
    <div class="btn">Read More</div>
  </div>
</section>

<section class="methods on-dark">
  <h2 class="section-title" style="top:20px">Our Methods</h2>
  <div class="divider" style="top:66px"><span></span></div>
  <p class="methods-intro">There are two hair replacement methods surgeons use depending<br>on a patient's goals.</p>

  <div class="method" style="left:97px">
    <h4>FUT (Traditional Follicular Unit Transpant)</h4>
    <p class="lede">Can wear hair short. Leaves faint linear scar</p>
    <div class="steps">
      <div class="step-head" style="top:0">Step 1:</div>
      <div class="step-body">
        <div class="step-art" role="img" aria-label="Illustration of a strip of scalp removed from the back of the head"></div>
        <p class="step-text">Hair on back of head is trimmed and a narrow strip is surgically removed so that hair can grow through and camouflage the scar.</p>
      </div>
      <div class="step-head closed" style="top:194px">Step 2:</div>
      <div class="step-head closed" style="top:242px">Step 3:</div>
    </div>
  </div>

  <div class="method" style="left:622px">
    <h4>FUE (Follicular Unite Extraction)</h4>
    <p class="lede">Can wear hair buzzed. Leaves diffuse pinpoint scarring</p>
    <div class="steps">
      <div class="step-head" style="top:0">Step 1:</div>
      <div class="step-body">
        <div class="step-art" role="img" aria-label="Illustration of follicles extracted with a small punch device"></div>
        <p class="step-text">Donor area on back of head is shaved to allow hair to be extracted with a tiny punch device.</p>
      </div>
      <div class="step-head closed" style="top:194px">Step 2:</div>
      <div class="step-head closed" style="top:242px">Step 3:</div>
    </div>
  </div>
</section>

<section class="comparison">
  <h2 class="section-title" style="top:18px">Comparison</h2>
  <div class="divider" style="top:64px"><span></span></div>
  <table class="compare-table">
    <thead><tr><th class="c1">Type of Surgery</th><th class="c2">FUT (Strip Method)</th><th>FUE</th></tr></thead>
    <tbody>
      <tr><td>Surgery Results</td><td>Completely Natural</td><td>Completely Natural</td></tr>
      <tr><td>Shaving of Head Required</td><td>No</td><td>Yes</td></tr>
      <tr><td>Pain after the procedure</td><td>Minor</td><td>None</td></tr>
      <tr><td>Stitches required</td><td>Yes (back of head from donor area)</td><td>No</td></tr>
      <tr><td>Length of Surgery</td><td>4-6 hours</td><td>5-8 hours or longer</td></tr>
      <tr><td>Local Anesthesia</td><td>Yes</td><td>Yes</td></tr>
      <tr><td>Bleeding During Procedure</td><td>Minor</td><td>None</td></tr>
    </tbody>
  </table>
</section>

<section class="contact">
  <div class="contact-photo" role="img" aria-label="Blue-toned photo of a doctor consulting a worried male patient"></div>
  <div class="contact-panel">
    <h2 class="section-title">Contact Us</h2>
    <div class="divider" style="top:60px"><span></span></div>
    <div class="field" style="top:116px">Name</div>
    <div class="field" style="top:167px">Email</div>
    <div class="field" style="top:219px">Phone Number</div>
    <div class="field message" style="top:270px">Message</div>
    <div class="submit">Submit Now</div>
    <span class="social" style="left:238px"></span>
    <span class="social" style="left:284px"></span>
    <span class="social" style="left:330px"></span>
    <span class="social" style="left:374px"></span>
  </div>
</section>

<section class="testimonials">
  <h2 class="section-title" style="top:28px">Testimonials</h2>
  <div class="divider" style="top:74px"><span></span></div>

  <div class="testimonial" style="left:97px">
    <div class="testimonial-photo" role="img" aria-label="Before and after photos of a patient's hairline" style="background:linear-gradient(90deg,#a8a5a3,#c9c5c2 50%,#a8a5a3)"></div>
    <div class="ba-bar"><span>BEFORE</span><span>AFTER</span></div>
    <p>Nemo enim ipsam voluptatem quia voluptas sit aspernatur aut odit aut fugit</p>
  </div>
  <div class="testimonial" style="left:442px">
    <div class="testimonial-photo" role="img" aria-label="Before and after photos of a patient's crown" style="background:linear-gradient(90deg,#d8d4d2,#b9a79c 50%,#d8d4d2)"></div>
    <div class="ba-bar"><span>BEFORE</span><span>AFTER</span></div>
    <p>Nemo enim ipsam voluptatem quia voluptas sit aspernatur aut odit aut fugit</p>
  </div>
  <div class="testimonial" style="left:787px">
    <div class="testimonial-photo" role="img" aria-label="Before and after photos of a patient with receding hair" style="background:linear-gradient(90deg,#c99b80,#e6d1c4 50%,#c99b80)"></div>
    <div class="ba-bar"><span>BEFORE</span><span>AFTER</span></div>
    <p>Nemo enim ipsam voluptatem quia voluptas sit aspernatur aut odit aut fugit</p>
  </div>
</section>

<section class="blog on-dark">
  <h2 class="section-title" style="top:20px">Our Blog</h2>
  <div class="divider" style="top:66px"><span></span></div>

  <article class="post" style="left:97px">
    <div class="post-photo" role="img" aria-label="Photo of a doctor consulting a male patient" style="background:linear-gradient(120deg,#e3e3e3,#b7b2ae)"></div>
    <h5>Nemo enim ipsam voluptatem</h5>
    <p>Nemo enim ipsam voluptatem quia volup tas sit aspernatur aut odit aut fugit, quia consequ untur magni dolores</p>
    <div class="more">Read More</div>
  </article>
  <article class="post" style="left:454px">
    <div class="post-photo" role="img" aria-label="Photo of a doctor examining a patient's scalp" style="background:linear-gradient(120deg,#a29b95,#d8d2cc)"></div>
    <h5>Nemo enim ipsam voluptatem</h5>
    <p>Nemo enim ipsam voluptatem quia volup tas sit aspernatur aut odit aut fugit, quia consequ untur magni dolores</p>
    <div class="more">Read More</div>
  </article>
  <article class="post" style="left:804px">
    <div class="post-photo" role="img" aria-label="Photo of a man checking his thinning hairline" style="background:linear-gradient(120deg,#cfa58d,#eee4de)"></div>
    <h5>Nemo enim ipsam voluptatem</h5>
    <p>Nemo enim ipsam voluptatem quia volup tas sit aspernatur aut odit aut fugit, quia consequ untur magni dolores</p>
    <div class="more">Read More</div>
  </article>
</section>

<footer class="footer">©2016 Hanul Hair Restoration Center. All Right Reserved</footer>

</body>
</html>
```